Realty Group Needs Classy, Contemporary Letterhead Design

We need a letterhead design for a new realty company located in NY, USA. We buy investment properties to rehabilitate and or keep in our rental portfolio.

```html
<!DOCTYPE html>
<html lang="en">
<head>
<meta charset="utf-8">
<title>Meridian Realty Group – Letterhead</title>
<link rel="stylesheet" href="https://fonts.googleapis.com/css2?family=Montserrat:wght@500;800&family=Arimo:wght@400&display=swap">
<style>
  :root {
    --brand-purple: #4f3a82;
    --ink: #2b2b2b;
    --muted-grey: #6f6f6f;
    --rule-grey: #9a9a9a;
    --page-white: #ffffff;
    --backdrop: #e6e7e9;
    --watermark-light: #f1f1f1;
    --watermark: #e8e8e8;
  }
  * { margin: 0; padding: 0; box-sizing: border-box; }
  html, body {
    width: 1000px;
    height: 1200px;
    overflow: hidden;
    background: var(--backdrop);
  }
  .letterhead {
    position: absolute;
    left: 85px;
    top: 68px;
    width: 812px;
    height: 1050px;
    background: var(--page-white);
    overflow: hidden;
  }
  .brand {
    position: absolute;
    left: 45px;
    top: 76px;
    width: 195px;
    text-align: center;
  }
  .brand-name {
    display: block;
    font-family: "Montserrat", sans-serif;
    font-weight: 800;
    font-size: 31px;
    line-height: 32px;
    letter-spacing: 0.3px;
    color: var(--brand-purple);
  }
  .brand-sub {
    display: flex;
    align-items: center;
    gap: 6px;
    margin-top: 1px;
    font-family: "Montserrat", sans-serif;
    font-weight: 500;
    font-size: 9.5px;
    letter-spacing: 0.6px;
    color: var(--muted-grey);
    white-space: nowrap;
  }
  .brand-sub::before,
  .brand-sub::after {
    content: "";
    flex: 1;
    height: 1px;
    background: var(--rule-grey);
  }
  .address {
    position: absolute;
    right: 214px;
    top: 105px;
    text-align: right;
    font-family: "Arimo", sans-serif;
    font-style: normal;
    font-size: 13px;
    line-height: 16px;
    color: var(--ink);
  }
  .address-icon {
    width: 14px;
    height: 13px;
    vertical-align: -1px;
    margin-right: 4px;
    fill: var(--brand-purple);
  }
  .divider {
    position: absolute;
    left: 606px;
    top: 58px;
    width: 1px;
    height: 80px;
    background: var(--rule-grey);
  }
  .contact-list {
    position: absolute;
    right: 0;
    top: 38px;
    list-style: none;
  }
  .contact-item {
    display: flex;
    justify-content: flex-end;
    align-items: center;
    height: 26px;
    font-family: "Arimo", sans-serif;
    font-size: 13px;
    color: var(--ink);
  }
  .contact-tab {
    width: 53px;
    height: 13px;
    margin-left: 8px;
    background: var(--brand-purple);
    display: flex;
    align-items: center;
    padding-left: 5px;
  }
  .contact-tab svg {
    width: 9px;
    height: 9px;
    fill: none;
    stroke: #fff;
    stroke-width: 1.3;
  }
  .watermark-art {
    position: absolute;
    left: 85px;
    top: 542px;
    width: 630px;
    height: 508px;
    border-radius: 50% 50% 0 0 / 60% 60% 0 0;
    background: linear-gradient(180deg, var(--watermark-light) 0%, var(--watermark) 100%);
  }
</style>
</head>
<body>
  <main class="letterhead">
    <header>
      <div class="brand">
        <span class="brand-name">MERIDIAN</span>
        <span class="brand-sub">Realty Group, LLC</span>
      </div>

      <address class="address">
        <svg class="address-icon" viewBox="0 0 13 12" aria-hidden="true"><path d="M6.5 0 0 6h2v6h3.5V8h2v4H11V6h2z"/></svg>00, xxxxxx, xxxxxxx<br>
        xxxxxxx-0000
      </address>

      <div class="divider"></div>

      <ul class="contact-list">
        <li class="contact-item">00 000 0000
          <span class="contact-tab"><svg viewBox="0 0 10 10" aria-hidden="true"><path d="M2 1c1 0 1.5 2 1 2.5S3 5 5 7s2.5 1.5 3 1S9 9 9 9 7.5 10 4 6.5 1 1 2 1z"/></svg></span>
        </li>
        <li class="contact-item">0000000000
          <span class="contact-tab"><svg viewBox="0 0 10 10" aria-hidden="true"><rect x="2.5" y="0.8" width="5" height="8.4" rx="0.8"/></svg></span>
        </li>
        <li class="contact-item">xxxxx@xxxx.xxx
          <span class="contact-tab"><svg viewBox="0 0 10 10" aria-hidden="true"><rect x="0.8" y="2" width="8.4" height="6"/><path d="M0.8 2 5 5.5 9.2 2"/></svg></span>
        </li>
        <li class="contact-item">xxx.xxxxxxxxxxxxx.xxx
          <span class="contact-tab"><svg viewBox="0 0 10 10" aria-hidden="true"><circle cx="5" cy="5" r="4"/><path d="M1 5h8M5 1c-2 2.5-2 5.5 0 8M5 1c2 2.5 2 5.5 0 8"/></svg></span>
        </li>
      </ul>
    </header>

    <div class="watermark-art" role="img" aria-label="Large faint light-grey silhouette illustration of an archer centaur drawing a bow, set as a background watermark"></div>
  </main>
</body>
</html>
```